Mira Glow Opening Flyer (German Text Involved!)

We need a double-sided flyer design for a new beauty studio in Zurich, Switzerland called "Mira Glow" our services are Laser Hair Removal, Diode Laser, Manicure, Pedicure, Massage, Makeup, Facial, and Waxing. Our main service is Laser Hair Removal. We would like to see designs that use the colors purple and white. The final design should communicate beauty for men and women. You will find the Logo in the attachments.

The flyer must be 105mm wide x 210mm tall.

The following text must be on the flyer:

FRONT TEXT:
Unser “Mira Glow“ Studio liegt beim Haltestelle Lindenpark. Wir sind dein Partner für natürliche Schönheit, ob Haut, Nägel, Wimpern oder Haarentfernungen. Wir verschönern dein Aussehen mit professionellen Behandlungen.

Eröffnungsrabatt von 20% für Neukunden bis Ende November 2020 auf Diodenlaser-Behandlungen.

Wir freuen uns auf deinen Besuch.

Mira Glow, Lindenweg 27, 8600 Dübendorf, Tel. 044 382 17 49

www.mira-glow-studio.ch

BACK TEXT:
DIENSTLEISTUNGEN

Pediküre:
Auch Füsse brauchen Pflege. Die Pediküre mit erfrischendem Bad und kosmetischer Pflege zaubert Füsse, die sich sehen lassen können.

Maniküre:
Gepflegte Hände sind nicht nur unsere Visitenkarte, sie geben uns auch den ganzen Tag ein gutes Gefühl.

Haarentfernung:
Als attraktiv und ästhetisch gelten nicht nur eine gute Figur, sondern auch eine glatte, unbehaarte Haut, speziell für Frauen, aber zunehmend auch für Männer.

Wimpern-Lifting:
Voluminöse Wimpern geben den Augen Ausdrucksstärke und wirken verführerisch. Mit einem professionellen Wimpern-Lifting wird dieser Effekt noch verstärkt.

Maniküre, schon ab CHF 45.-
Pediküre, schon ab CHF 60.-
Dauerhafte Haarentfernung mit dem Diodenlaser, schon ab CHF 25.-
Haarentfernung mit Wachs, schon ab CHF 15.-

UNSERE ÖFFNUNGSZEITEN
Montag bis Samstag
09:00 bis 18:00

www.mira-glow-studio.ch

Target Market(s)

beauty for men and women

Industry/Entity Type

Beauty Salon

Colors
876aae

Requirements
Must have
• FRONT TEXT:

www.mira-glow-studio.ch

BACK TEXT:
DIENSTLEISTUNGEN

Pediküre:

Maniküre:

Haarentfernung:

Wimpern-Lifting:

UNSERE ÖFFNUNGSZEITEN
Montag bis Samstag
09:00 bis 18:00

www.mira-glow-studio.ch

```html
<!DOCTYPE html>
<html lang="de">
<head>
<meta charset="utf-8">
<title>Mira Glow – Eröffnungsflyer</title>
<link rel="stylesheet" href="https://fonts.googleapis.com/css2?family=Montserrat:wght@400;500;600;700&family=Lobster+Two:ital,wght@1,700&family=Great+Vibes&family=Oswald:wght@400&display=swap">
<style>
:root{
  --purple:#643695;
  --purple-line:#8a6cb8;
  --lilac:#b9a3d6;
  --magenta:#c4267f;
  --pink:#e5348e;
  --orange:#f7931e;
  --white:#ffffff;
  --ink:#2b2b2b;
  --backdrop:#ececec;
}
*{box-sizing:border-box;margin:0;padding:0}
html,body{width:1200px;height:993px;overflow:hidden;background:var(--backdrop);font-family:"Montserrat",sans-serif}
.flyer{position:absolute;top:102px;width:382px;height:763px;overflow:hidden;background:var(--white)}
.flyer--front{left:98px}
.flyer--back{left:543px}
.flyer svg.art{position:absolute;inset:0}
.abs{position:absolute}

/* front */
.brand{left:0;right:0;top:46px;text-align:center;color:var(--white);font-weight:600;font-size:32px;letter-spacing:1px;display:flex;justify-content:center;align-items:center;gap:12px}
.brand-dot{width:34px;height:34px;border:2px solid var(--white);border-radius:50%}
.intro{left:20px;right:20px;top:106px;text-align:center;color:var(--white);font-family:"Lobster Two",cursive;font-style:italic;font-weight:700;font-size:17.2px;line-height:23.5px}
.offer-kicker{left:20px;width:182px;top:402px;text-align:center;color:var(--white);font-size:11.5px}
.offer-head{left:20px;width:182px;top:427px;text-align:center;color:var(--purple);font-family:"Oswald",sans-serif;font-size:25px;line-height:32px}
.offer-body{left:20px;width:182px;top:462px;text-align:center;color:var(--white);font-size:11.3px;line-height:15.8px}
.welcome{left:0;right:0;top:612px;text-align:center;color:var(--white);font-family:"Great Vibes",cursive;font-size:31px;white-space:nowrap}
.sign{left:0;right:0;top:660px;text-align:center;color:var(--white);font-weight:600;font-size:21px}
.address{left:0;right:0;top:698px;text-align:center;color:var(--white);font-size:14px;display:flex;justify-content:center;align-items:center;gap:6px;white-space:nowrap}

.contact{left:24px;width:334px;top:719px;height:27px;border-radius:14px;background:var(--white);display:flex;align-items:center;overflow:hidden;white-space:nowrap}
.contact-phone{flex-shrink:0;background:var(--pink);height:100%;display:flex;align-items:center;gap:6px;padding:0 12px 0 2px;color:var(--white);font-weight:500;font-size:13px;letter-spacing:.3px}
.contact-web{flex-shrink:0;display:flex;align-items:center;gap:5px;padding-left:3px;color:var(--purple);font-weight:600;font-size:12px}
.icon-ring{flex-shrink:0;width:23px;height:23px;border-radius:50%;border:1.5px solid var(--purple);background:var(--white);display:flex;align-items:center;justify-content:center}
.contact-phone .icon-ring{border-color:var(--white);background:var(--pink)}

/* back */
.services-title{left:0;right:0;top:0;height:64px;background:var(--purple);color:var(--white);font-weight:600;font-size:25px;letter-spacing:4.5px;text-align:center;line-height:76px}
.service{left:0;right:0;position:absolute}
.service-thumb{position:absolute;left:31px;width:82px;height:82px;border-radius:50%;border:3px solid var(--lilac)}
.service-name{position:absolute;left:134px;width:220px;color:var(--purple);font-weight:500;font-size:15.5px;padding-bottom:3px;border-bottom:1px solid var(--purple-line)}
.service-text{position:absolute;left:135px;width:222px;color:var(--ink);font-size:10.2px;line-height:14.3px}

.prices{left:27px;width:327px;top:452px;list-style:none}
.price{display:flex;justify-content:space-between;align-items:center;border:1px solid var(--purple);border-radius:12px;margin-bottom:4px;height:20px;overflow:hidden}
.price--tall{height:34px;border-radius:17px}
.price-label{padding-left:16px;color:var(--purple);font-weight:500;font-size:11px;line-height:12.5px;white-space:nowrap}
.price-value{flex-shrink:0;background:var(--orange);color:var(--white);font-weight:700;font-size:11px;width:76px;height:100%;display:flex;align-items:center;justify-content:center;border-radius:12px}

.hours-title{left:0;right:0;top:627px;text-align:center;color:var(--white);font-weight:600;font-size:15px;letter-spacing:.6px}
.hours{left:27px;width:327px;top:647px;height:22px;border-radius:11px;background:var(--orange);color:var(--white);font-size:13px;font-weight:500;display:flex;align-items:center;padding-left:12px;gap:8px;white-space:nowrap}
.hours span+svg{margin-left:14px}
.footer-row{left:0;right:0;top:684px;display:flex;justify-content:center;align-items:center;gap:10px;color:var(--white)}
.footer-brand{font-weight:600;font-size:18px;padding-right:10px;border-right:1px solid var(--white);line-height:28px}
.footer-address{font-size:11px;line-height:14.5px}
</style>
</head>
<body>

<section class="flyer flyer--front">
  <svg class="art" viewBox="0 0 382 763" width="382" height="763">
    <defs>
      <radialGradient id="skinMan" cx=".5" cy=".45" r=".6"><stop offset="0" stop-color="#e9c3a8"/><stop offset=".7" stop-color="#c99579"/><stop offset="1" stop-color="#f3efee"/></radialGradient>
      <radialGradient id="skinWoman" cx=".5" cy=".45" r=".6"><stop offset="0" stop-color="#f6dccd"/><stop offset=".65" stop-color="#e9bfa6"/><stop offset="1" stop-color="#fbf7f5"/></radialGradient>
    </defs>
    <rect width="382" height="763" fill="var(--purple)"/>
    <path d="M0,270 C40,262 75,232 120,216 C170,200 230,248 290,238 C330,230 360,218 382,205 L382,560 C330,545 260,560 200,585 C140,610 60,580 0,540 Z" fill="var(--white)"/>
    <path d="M345,238 L382,205 L382,285 Z" fill="#d3ecf6"/>
    <path d="M0,270 L14,268 L6,320 L0,322 Z" fill="#d3ecf6"/>
    <circle cx="273" cy="360" r="165" fill="none" stroke="var(--orange)" stroke-width=".8"/>
    <circle cx="73" cy="302" r="86" fill="url(#skinMan)" role="img" aria-label="Foto: lächelnder Mann mit gepflegter Haut"/>
    <circle cx="273" cy="360" r="155" fill="url(#skinWoman)" role="img" aria-label="Foto: Frau mit strahlender Gesichtshaut"/>
    <circle cx="111" cy="464" r="91" fill="var(--orange)"/>
    <circle cx="111" cy="464" r="84" fill="none" stroke="var(--white)" stroke-width=".7"/>
    <path d="M14,428 L210,428 L207,461 L17,461 Z" fill="var(--white)"/>
    <path d="M0,548 C70,600 150,622 232,607 C292,596 332,560 382,552 L382,763 L0,763 Z" fill="var(--purple)"/>
    <path d="M0,533 C70,578 150,602 232,588 C292,577 332,548 382,545 L382,553 C332,558 292,592 232,604 C150,618 70,598 0,547 Z" fill="var(--magenta)"/>
    <circle cx="293" cy="544" r="48" fill="#7cc26a" opacity=".6"/>
    <circle cx="209" cy="568" r="33" fill="var(--orange)" opacity=".55"/>
  </svg>

  <div class="abs brand"><span class="brand-dot"></span>Mira Glow</div>
  <p class="abs intro">Wir sind dein Partner für<br>natürliche Schönheit, ob Haut, Nägel, Wimpern<br>oder Haarentfernungen. Wir verschönern dein<br>Aussehen mit professionellen Behandlungen.</p>

  <p class="abs offer-kicker">Eröffnungsrabatt</p>
  <p class="abs offer-head">VON 20% FÜR</p>
  <p class="abs offer-body">Neukunden bis<br>Ende November 2020<br>auf Diodenlaser-<br>Behandlungen.</p>

  <p class="abs welcome">Wir freuen uns auf deinen Besuch.</p>
  <p class="abs sign">Mira Glow</p>
  <p class="abs address">
    <svg width="9" height="12" viewBox="0 0 9 12"><path d="M4.5 0A4.5 4.5 0 0 0 0 4.5C0 8 4.5 12 4.5 12S9 8 9 4.5A4.5 4.5 0 0 0 4.5 0Zm0 6.3a1.8 1.8 0 1 1 0-3.6 1.8 1.8 0 0 1 0 3.6Z" fill="#fff"/></svg>
    Lindenweg 27, 8600 Dübendorf,
  </p>
  <div class="abs contact">
    <div class="contact-phone">
      <span class="icon-ring"><svg width="11" height="11" viewBox="0 0 24 24"><path d="M6.6 10.8a15 15 0 0 0 6.6 6.6l2.2-2.2c.3-.3.7-.4 1-.2 1.1.4 2.3.6 3.6.6.6 0 1 .4 1 1V20c0 .6-.4 1-1 1A17 17 0 0 1 3 4c0-.6.4-1 1-1h3.5c.6 0 1 .4 1 1 0 1.3.2 2.5.6 3.6.1.3 0 .7-.2 1Z" fill="#fff"/></svg></span>
      <span>044 382 17 49</span>
    </div>
    <div class="contact-web">
      <span class="icon-ring"><svg width="11" height="11" viewBox="0 0 24 24"><path d="M5 19l4-1 10-10-3-3L6 15Z" fill="none" stroke="#643695" stroke-width="2"/></svg></span>
      <span>www.mira-glow-studio.ch</span>
    </div>
  </div>
</section>

<section class="flyer flyer--back">
  <svg class="art" viewBox="0 0 382 763" width="382" height="763">
    <path d="M0,612 C80,628 170,568 245,563 C305,560 350,585 382,605 L382,763 L0,763 Z" fill="var(--purple)"/>
    <path d="M0,596 C80,612 165,552 240,546 C305,542 352,570 382,595 L382,604 C350,582 305,558 240,562 C165,567 80,628 0,611 Z" fill="var(--magenta)"/>
  </svg>

  <h1 class="abs services-title">DIENSTLEISTUNGEN</h1>

  <div class="service">
    <div class="service-thumb" style="top:76px;background:radial-gradient(circle,#f3d8c9,#e7c4b8 60%,#f7eeee)" role="img" aria-label="Foto: gepflegte Füsse bei der Pediküre"></div>
    <h2 class="service-name" style="top:70px">Pediküre:</h2>
    <p class="service-text" style="top:102px">Auch Füsse brauchen Pflege. Die Pediküre mit erfrischendem Bad und kosmetischer Pflege zaubert Füsse, die sich sehen lassen können.</p>
  </div>
  <div class="service">
    <div class="service-thumb" style="top:166px;background:radial-gradient(circle,#f5dccd,#eac8b5 60%,#faf5f2)" role="img" aria-label="Foto: Hände mit French-Maniküre"></div>
    <h2 class="service-name" style="top:168px">Maniküre:</h2>
    <p class="service-text" style="top:200px">Gepflegte Hände sind nicht nur unsere Visitenkarte, sie geben uns auch den ganzen Tag ein gutes Gefühl.</p>
  </div>
  <div class="service">
    <div class="service-thumb" style="top:256px;background:radial-gradient(circle,#f1cdbd,#dca896 60%,#ead7d0)" role="img" aria-label="Foto: glatte Haut nach der Haarentfernung"></div>
    <h2 class="service-name" style="top:251px">Haarentfernung:</h2>
    <p class="service-text" style="top:283px">Als attraktiv und ästhetisch gelten nicht nur eine gute Figur, sondern auch eine glatte, unbehaarte Haut, speziell für Frauen, aber zunehmend auch für Männer.</p>
  </div>
  <div class="service">
    <div class="service-thumb" style="top:355px;background:radial-gradient(circle,#c9d4dd,#8d8f96 55%,#e4e1e3)" role="img" aria-label="Foto: Auge mit gelifteten Wimpern"></div>
    <h2 class="service-name" style="top:350px">Wimpern-Lifting:</h2>
    <p class="service-text" style="top:382px">Voluminöse Wimpern geben den Augen Ausdrucksstärke und wirken verführerisch. Mit einem professionellen Wimpern-Lifting wird dieser Effekt noch verstärkt.</p>
  </div>

  <ul class="abs prices">
    <li class="price"><span class="price-label">Maniküre, schon ab</span><span class="price-value">CHF 45.-</span></li>
    <li class="price"><span class="price-label">Pediküre, schon ab</span><span class="price-value">CHF 60.-</span></li>
    <li class="price price--tall"><span class="price-label">Dauerhafte Haarentfernung mit dem<br>Diodenlaser, schon ab</span><span class="price-value">CHF 25.-</span></li>
    <li class="price"><span class="price-label">Haarentfernung mit Wachs, schon ab</span><span class="price-value">CHF 15.-</span></li>
  </ul>

  <h2 class="abs hours-title">UNSERE ÖFFNUNGSZEITEN</h2>
  <div class="abs hours">
    <svg width="16" height="16" viewBox="0 0 16 16"><rect x="1" y="2.5" width="14" height="12" rx="1.5" fill="none" stroke="#fff"/><line x1="1" y1="6" x2="15" y2="6" stroke="#fff"/><line x1="4.5" y1="1" x2="4.5" y2="4" stroke="#fff"/><line x1="11.5" y1="1" x2="11.5" y2="4" stroke="#fff"/></svg>
    <span>Montag bis Samstag</span>
    <svg width="16" height="16" viewBox="0 0 16 16"><circle cx="8" cy="8" r="7" fill="none" stroke="#fff"/><circle cx="8" cy="8" r="5" fill="none" stroke="#fff" stroke-width=".6"/><path d="M8 4.5V8l2.2 1.5" fill="none" stroke="#fff"/></svg>
    <span>09:00 bis 18:00</span>
  </div>
  <div class="abs footer-row">
    <span class="footer-brand">Mira Glow</span>
    <p class="footer-address">
      <svg width="7" height="10" viewBox="0 0 9 12"><path d="M4.5 0A4.5 4.5 0 0 0 0 4.5C0 8 4.5 12 4.5 12S9 8 9 4.5A4.5 4.5 0 0 0 4.5 0Zm0 6.3a1.8 1.8 0 1 1 0-3.6 1.8 1.8 0 0 1 0 3.6Z" fill="#fff"/></svg>
      Lindenweg 27,<br>8600 Dübendorf,
    </p>
  </div>
  <div class="abs contact">
    <div class="contact-phone">
      <span class="icon-ring"><svg width="11" height="11" viewBox="0 0 24 24"><path d="M6.6 10.8a15 15 0 0 0 6.6 6.6l2.2-2.2c.3-.3.7-.4 1-.2 1.1.4 2.3.6 3.6.6.6 0 1 .4 1 1V20c0 .6-.4 1-1 1A17 17 0 0 1 3 4c0-.6.4-1 1-1h3.5c.6 0 1 .4 1 1 0 1.3.2 2.5.6 3.6.1.3 0 .7-.2 1Z" fill="#fff"/></svg></span>
      <span>044 382 17 49</span>
    </div>
    <div class="contact-web">
      <span class="icon-ring"><svg width="11" height="11" viewBox="0 0 24 24"><path d="M5 19l4-1 10-10-3-3L6 15Z" fill="none" stroke="#643695" stroke-width="2"/></svg></span>
      <span>www.mira-glow-studio.ch</span>
    </div>
  </div>
</section>

</body>
</html>
```